Design A HVAC Business Website with Figma

We are launching a Web Design Service for HVAC and other Home Improvement businesses. We need to create some demo sites. These sites will be used to develop Webflow templates, so they must look very professional and real.

I am providing some sample data for this design. **,DO NOT USE LOREM IPSUM** anywhere in this design. We will be featuring these designs on our website and marketing materials.

More information can be found on this Notion page https://pallid-cove-q29.wikinest.example/Web-Design-Project-7d2a9e1f04b8c365a1e9d70f42c6b8e3

Industry/Entity Type

HVAC, Plumbing, Remodeling, General Contractor

Number of Pages Required

5+ page

Requirements
Must have
• Must be professional

```html
<!DOCTYPE html>
<html lang="en">
<head>
<meta charset="utf-8">
<title>Harborline HVAC</title>
<link href="https://fonts.googleapis.com/css2?family=Poppins:wght@400;500;600;700;800&display=swap" rel="stylesheet">
<style>
:root{
  --red:#d71920;
  --navy:#0c2a57;
  --deep:#0a2350;
  --blue:#1d5fb8;
  --ink:#1c1c1c;
  --grey:#e9eaec;
  --line:#b9c3d3;
  --white:#ffffff;
}
*{box-sizing:border-box;margin:0;padding:0}
html,body{width:1200px;height:2884px;overflow:hidden}
body{font-family:'Poppins',sans-serif;color:var(--ink);background:var(--white);position:relative}
.topbar{position:absolute;top:0;left:0;width:1200px;height:54px;display:flex;align-items:center;justify-content:space-between;padding:0 70px 0 110px}
.topbar .emergency{color:var(--red);font-weight:600;font-size:24px}
.topbar .call{font-weight:700;font-size:17px;color:var(--navy);display:flex;align-items:center;gap:18px}
.topbar .call strong{color:var(--red);font-size:28px;font-weight:700}
.nav{position:absolute;top:54px;left:100px;width:1030px;height:60px;background:var(--navy);border-radius:30px;display:flex;align-items:center;padding:0 40px;z-index:3}
.nav .brand{color:var(--white);font-weight:700;font-size:26px;margin-right:auto}
.nav a{color:var(--white);font-size:15px;font-weight:600;text-decoration:none;margin-left:38px;text-transform:uppercase}
.nav .contact{background:var(--red);padding:8px 28px;border-radius:18px;margin-left:44px}
.hero{position:absolute;top:0;left:0;width:1200px;height:720px;background:linear-gradient(90deg,rgba(255,255,255,.95) 0,rgba(255,255,255,.85) 34%,rgba(255,255,255,0) 50%),linear-gradient(120deg,#d9c7ae,#b48d63 45%,#7b8a98 80%,#5c6a78)}
.hero-photo{position:absolute;top:0;left:0;width:100%;height:100%}
.hero-copy{position:absolute;left:110px;top:168px;width:520px}
.hero .eyebrow{font-size:17px;font-weight:700;color:var(--navy)}
.hero h1{font-size:58px;line-height:1.08;font-weight:800;color:var(--red);text-transform:uppercase;margin-top:12px}
.hero p{font-size:17px;line-height:1.45;font-weight:600;margin-top:22px;color:var(--ink)}
.btn{display:inline-block;background:var(--red);color:var(--white);font-weight:700;font-size:15px;padding:14px 36px;border-radius:28px;text-transform:uppercase;margin-top:40px}
.ready{position:absolute;top:720px;left:0;width:1200px;height:460px;background:linear-gradient(90deg,#e6e8ea,#f4f5f6 60%,#e9eaec)}
.ready .photo{position:absolute;left:0;top:0;width:620px;height:460px;background:linear-gradient(110deg,#d7dadc,#c7b9a6 40%,#e9ecef)}
.ready .copy{position:absolute;left:660px;top:70px;width:470px}
.ready h2{font-size:48px;font-weight:700;color:var(--blue);line-height:1.1}
.ready p{font-size:18px;line-height:1.45;margin-top:30px}
.why{position:absolute;top:1180px;left:0;width:1200px;height:540px;background:var(--white)}
.why h2{position:absolute;left:180px;top:36px;font-size:36px;font-weight:700;color:var(--red)}
.grid{position:absolute;left:120px;top:108px;display:grid;grid-template-columns:272px 272px;column-gap:28px;row-gap:22px}
.grid div{height:72px;border:2px solid var(--line);border-radius:12px;display:flex;align-items:center;justify-content:center;text-align:center;font-size:16px;font-weight:600;line-height:1.3;padding:0 16px;box-shadow:0 3px 6px rgba(0,0,0,.08)}
.why .tech{position:absolute;left:760px;top:80px;width:340px;height:460px;background:linear-gradient(180deg,#eef1f5,#c9d3e0 60%,#2a63b5)}
.services{position:absolute;top:1720px;left:0;width:1200px;height:730px;background:linear-gradient(180deg,#c9ccd1,#e3e5e8 45%,#cfd2d6)}
.services h2{position:absolute;left:0;width:1200px;top:46px;text-align:center;font-size:44px;font-weight:700;color:var(--red)}
.cards{position:absolute;left:108px;top:132px;display:flex;gap:28px}
.card{width:236px;height:480px;background:var(--white);border-radius:14px;padding:12px;text-align:center;box-shadow:0 4px 12px rgba(0,0,0,.12)}
.card .img{height:190px;border-radius:10px}
.card h3{font-size:21px;font-weight:700;color:var(--red);margin-top:26px;line-height:1.2}
.card p{font-size:13px;line-height:1.45;margin-top:10px}
.footer{position:absolute;top:2450px;left:0;width:1200px;height:434px;background:var(--deep)}
</style>
</head>
<body>
<section class="hero">
  <div class="hero-photo" role="img" aria-label="Photo of children playing on a living room floor with a toy car"></div>
  <div class="hero-copy">
    <div class="eyebrow">WITH SAN DIEGO'S MOST TRUSTED HVAC COMPANY</div>
    <h1>Keep always a great weather for your family</h1>
    <p>Welcome to Harborline HVAC, your trusted source for heating, ventilation, and air conditioning services in San Diego County. Our team of certified technicians has been providing top-notch service to our customers for over 13 years.</p>
    <span class="btn">Shedule your inspection</span>
  </div>
</section>
<header class="topbar">
  <span class="emergency">24/7 Emergency Services</span>
  <span class="call">CALL US TODAY <strong>1-555-014-9200</strong></span>
</header>
<nav class="nav">
  <span class="brand">Harborline HVAC</span>
  <a href="#">About us</a><a href="#">Services</a><a href="#">Products</a><a href="#">Reviews</a>
  <a href="#" class="contact">Contact us</a>
</nav>
<section class="ready">
  <div class="photo" role="img" aria-label="Photo of a smiling technician giving a thumbs up beside a wall air conditioner"></div>
  <div class="copy">
    <h2>Ready to serve you</h2>
    <p>At Harborline HVAC, we believe in providing personalized service that meets the unique needs of our customers. We know that HVAC problems can be stressful and disruptive to your daily routine, which is why we offer flexible scheduling and 24/7 emergency services to ensure that we are always available when you need us.</p>
  </div>
</section>
<section class="why">
  <h2>Why Choose Harborline HVAC?</h2>
  <div class="grid">
    <div>Experienced and certified technicians</div><div>24/7 emergency services</div>
    <div>High-quality equipment and parts</div><div>Upfront pricing</div>
    <div>Flexible scheduling</div><div>Satisfaction Guarantee</div>
    <div>Personalized service</div><div>Personalized service</div>
  </div>
  <div class="tech" role="img" aria-label="Photo of a technician in a blue uniform and cap holding flexible ducting"></div>
</section>
<section class="services">
  <h2>Our Services:</h2>
  <div class="cards">
    <div class="card">
      <div class="img" role="img" aria-label="Photo of a technician servicing a furnace" style="background:linear-gradient(135deg,#6d7f8f,#2f4a66)"></div>
      <h3>Heating Services</h3>
      <p>Whether you need a new furnace installed, an old system repaired, or routine maintenance, our team has the expertise to keep you warm and cozy all winter long.</p>
    </div>
    <div class="card">
      <div class="img" role="img" aria-label="Photo of air conditioning units" style="background:linear-gradient(135deg,#3a5f8c,#9fb3c8)"></div>
      <h3>Air Conditioning Services</h3>
      <p>Stay cool and comfortable all summer long with our expert AC services. We offer installation, repair, and maintenance services for all types of AC units.</p>
    </div>
    <div class="card">
      <div class="img" role="img" aria-label="Photo of a hand cleaning an air vent" style="background:linear-gradient(135deg,#dfe4ea,#8e9aa8)"></div>
      <h3>Indoor Air Quality</h3>
      <p>We know that indoor air quality is essential for your health and comfort. Our team can help you improve your indoor air quality by installing air purifiers, humidifiers, and ventilation systems.</p>
    </div>
    <div class="card">
      <div class="img" role="img" aria-label="Photo of commercial rooftop HVAC equipment" style="background:linear-gradient(135deg,#4a6fa5,#1f3b66)"></div>
      <h3>Commercial HVAC</h3>
      <p>Our commercial HVAC services are designed to keep your business running smoothly. From routine maintenance to complex installations, our team can handle it all.</p>
    </div>
  </div>
</section>
<footer class="footer"></footer>
</body>
</html>
```